Velbrook App Homepage Design making customers feel in control of their spend

Hi,
We need a App Homepage design with a UI similar to the attached mock up on an Quillo 4. The app is intended to put customers in control of their usage and spend on their fixed phone, broadband, mobile, gas and electricity.

Please fee free to propose improvements to the background images, icons, colours, etc.

Any questions please let me know.

Thanks
Tomasz

Target Market(s)

Consumer customers

Industry/Entity Type

Internet

Font styles to use
Sans Serif

Colors
3276b5
0255a3
85acd3
cfdeed
ffffff

Requirements
Must have
• Content in line with the guidelines in the attached mock up

```html
<!DOCTYPE html>
<html lang="en">
<head>
<meta charset="utf-8">
<title>Velbrook – Home</title>
<link rel="stylesheet" href="https://fonts.googleapis.com/css2?family=Open+Sans:wght@300;400;600;700&display=swap">
<style>
  :root {
    --brand-deep: #0255a3;
    --brand-mid: #3276b5;
    --brand-soft: #85acd3;
    --brand-pale: #cfdeed;
    --white: #ffffff;
    --menu-grey: #c4c4c4;
    --card-line: #e3e8ee;
    --slice-electricity: #0457a5;
    --slice-gas: #b072d9;
    --slice-mobile: #36bf18;
    --slice-calls: #d05b47;
    --slice-fibre: #cfa946;
  }
  * { margin: 0; padding: 0; box-sizing: border-box; }
  html, body { width: 668px; height: 1200px; overflow: hidden; background: var(--white); }
  body { font-family: "Open Sans", Arial, sans-serif; position: relative; }

  .menu-toggle { position: absolute; left: 24px; top: 22px; width: 53px; height: 46px;
    display: flex; flex-direction: column; justify-content: space-between; }
  .menu-toggle span { display: block; height: 7px; background: var(--menu-grey); border-radius: 2px; }

  .brand { position: absolute; left: 0; right: 0; top: 118px; display: flex;
    justify-content: center; align-items: center; gap: 26px; }
  .brand-dot { width: 96px; height: 96px; border-radius: 50%; background: var(--brand-mid); }
  .brand-name { font-size: 78px; font-weight: 700; color: var(--brand-deep); letter-spacing: -1px; line-height: 1; }

  .greeting { position: absolute; left: 0; right: 0; top: 240px; text-align: center;
    font-size: 30px; font-weight: 400; color: var(--brand-soft); }
  .welcome { position: absolute; left: 0; right: 0; top: 276px; text-align: center;
    font-size: 40px; font-weight: 400; color: #7aa3cd; }

  .support-button { position: absolute; left: 88px; top: 358px; width: 505px; height: 68px;
    border: 2px solid var(--card-line); border-radius: 14px; display: flex; align-items: center;
    justify-content: center; font-size: 29px; color: var(--brand-mid); background: var(--white); }

  .spend-chart { position: absolute; left: 120px; top: 478px; width: 424px; height: 424px; }
  .slice-label { fill: var(--white); font-family: "Open Sans", Arial, sans-serif;
    font-size: 23px; font-weight: 600; text-anchor: middle; }

  .total-title { position: absolute; left: 0; right: 0; top: 976px; text-align: center;
    font-size: 40px; font-weight: 300; color: var(--brand-soft); }
  .total-amount { position: absolute; left: 0; right: 0; top: 1026px; text-align: center;
    font-size: 38px; font-weight: 700; color: var(--brand-deep); }

  .bill-info { position: absolute; left: 88px; top: 1088px; width: 505px; height: 86px;
    border: 2px solid var(--card-line); border-radius: 14px; display: flex; flex-direction: column;
    align-items: center; justify-content: center; font-size: 23px; line-height: 1.3; color: var(--brand-mid); }
</style>
</head>
<body>
  <div class="menu-toggle" aria-label="Menu"><span></span><span></span><span></span></div>

  <header class="brand">
    <div class="brand-dot"></div>
    <div class="brand-name">Velbrook</div>
  </header>

  <p class="greeting">Good Morning Marla !</p>
  <h1 class="welcome">Welcome to Velbrook</h1>

  <div class="support-button">Call 24 / 7 Support</div>

  <svg class="spend-chart" viewBox="-212 -212 424 424" role="img" aria-label="Spend breakdown pie chart">
    <path d="M0 0 L0 -212 A212 212 0 0 1 205.3 52.7 Z" fill="var(--slice-electricity)"/>
    <path d="M0 0 L205.3 52.7 A212 212 0 0 1 124.6 171.5 Z" fill="var(--slice-gas)"/>
    <path d="M0 0 L124.6 171.5 A212 212 0 0 1 -124.6 171.5 Z" fill="var(--slice-mobile)"/>
    <path d="M0 0 L-124.6 171.5 A212 212 0 0 1 -208.2 -39.7 Z" fill="var(--slice-calls)"/>
    <path d="M0 0 L-208.2 -39.7 A212 212 0 0 1 0 -212 Z" fill="var(--slice-fibre)"/>
    <text class="slice-label" x="113" y="-64">Electricity<tspan x="113" dy="32">(29%)</tspan></text>
    <text class="slice-label" x="121" y="112">Gas<tspan x="121" dy="32">(11%)</tspan></text>
    <text class="slice-label" x="-20" y="141">Mobile<tspan x="-20" dy="32">(20%)</tspan></text>
    <text class="slice-label" x="-126" y="37">Calls<tspan x="-126" dy="32">(18%)</tspan></text>
    <text class="slice-label" x="-99" y="-96">Fibre<tspan x="-99" dy="32">(22%)</tspan></text>
  </svg>

  <p class="total-title">Your current total charges</p>
  <p class="total-amount">$ 68.39</p>

  <div class="bill-info">
    <span>Last Bill : $ 75.76 on 09 / 12 / 2016</span>
    <span>Allowance renews in 18 days</span>
  </div>
</body>
</html>
```